Business Card Design

Locksmith, Safes, Security Systems, Camera Systems, Home Theater, Chip Keys & Remotes

Industry/Entity Type

Business

Contact Information for Business Card

Dorian Pelley Owner
2870 Fenwick Hollow Loop
Dothan, AL 36301
P 334-555-0148
F 334-555-0193
dpelley@tamblynkeys.com
www.tamblynkeys.com
AL Lic #5827
*Maybe follow us on Socialpage or Socialpage symbol

```html
<!DOCTYPE html>
<html lang="en">
<head>
<meta charset="utf-8">
<title>Tamblyn's Lock &amp; Security – Business Card</title>
<link href="https://fonts.googleapis.com/css2?family=Oswald:wght@500&family=Roboto+Condensed:wght@300;400;700&display=swap" rel="stylesheet">
<style>
  :root {
    --brand-blue: #2d3a94;
    --ink-dark: #2a2a2a;
    --silver-light: #f7f7f7;
    --silver-mid: #d6d6d6;
    --silver-dark: #a9a9a9;
    --page: #ffffff;
  }
  * { margin: 0; padding: 0; box-sizing: border-box; }
  html, body { width: 1200px; height: 836px; overflow: hidden; background: var(--page); }
  .card {
    position: absolute; left: 117px; top: 129px; width: 861px; height: 548px;
    background: linear-gradient(90deg, var(--silver-mid) 0%, var(--silver-light) 22%, #ffffff 45%, #ffffff 60%, var(--silver-mid) 88%, var(--silver-dark) 100%);
    box-shadow: 8px 8px 14px rgba(0,0,0,.35);
    overflow: hidden;
    font-family: "Roboto Condensed", sans-serif;
  }
  .brand-mark { position: absolute; left: 28px; top: 34px; width: 93px; height: 93px; background: var(--brand-blue); }
  .brand-name {
    position: absolute; right: 524px; top: 72px; text-align: right;
    color: var(--brand-blue); font-weight: 400; text-transform: uppercase; white-space: nowrap;
  }
  .brand-name .line-main { display: block; font-size: 36px; line-height: 40px; }
  .brand-name .line-sub { display: block; font-size: 18px; line-height: 22px; margin-top: 2px; padding-right: 26px; }
  .divider { position: absolute; left: 352px; top: 80px; width: 4px; height: 303px; background: var(--brand-blue); }
  .person { position: absolute; right: 524px; top: 178px; text-align: right; white-space: nowrap; }
  .person-name { color: var(--brand-blue); font-weight: 700; font-size: 28px; line-height: 38px; }
  .person-title { color: var(--ink-dark); font-weight: 300; font-size: 29px; line-height: 40px; }
  .person-license { color: var(--brand-blue); font-weight: 400; font-size: 21px; line-height: 30px; margin-top: 8px; }
  .social { display: inline-flex; align-items: center; gap: 8px; margin-top: 24px; color: var(--brand-blue); font-size: 15px; }
  .social-square { width: 32px; height: 32px; border: 2px solid var(--brand-blue); border-radius: 3px; }
  .contact { position: absolute; left: 372px; top: 172px; list-style: none; }
  .contact li { display: flex; align-items: center; height: 42px; color: var(--ink-dark); font-weight: 300; font-size: 25px; white-space: nowrap; }
  .contact li.small { font-size: 23px; }
  .contact svg { width: 26px; height: 24px; margin-right: 16px; fill: none; stroke: var(--brand-blue); stroke-width: 2; flex: none; }
  .contact svg .solid { fill: var(--brand-blue); stroke: none; }
  .band { position: absolute; left: 0; top: 0; width: 861px; height: 548px; }
  .services {
    position: absolute; left: 0; width: 861px; top: 484px; height: 40px;
    display: flex; justify-content: center; align-items: center;
  }
  .services span {
    display: inline-block; flex: none; white-space: nowrap;
    color: #ffffff; font-family: "Oswald", sans-serif; font-weight: 500; font-size: 26px;
    transform: scaleX(.86);
  }
</style>
</head>
<body>
  <div class="card">
    <svg class="band" viewBox="0 0 861 548" aria-hidden="true">
      <defs>
        <linearGradient id="chrome" x1="0" x2="1">
          <stop offset="0" stop-color="#ffffff"/>
          <stop offset=".5" stop-color="#8c8c8c"/>
          <stop offset="1" stop-color="#ffffff"/>
        </linearGradient>
      </defs>
      <path d="M0 454 Q430 400 861 454 L861 472 Q430 418 0 472 Z" fill="url(#chrome)"/>
      <path d="M0 469 Q430 415 861 469 L861 548 L0 548 Z" fill="var(--brand-blue)"/>
    </svg>

    <div class="brand-mark"></div>
    <div class="brand-name"><span class="line-main">Tamblyn's</span><span class="line-sub">Lock &amp; Security</span></div>

    <div class="person">
      <div class="person-name">Dorian Pelley</div>
      <div class="person-title">Owner</div>
      <div class="person-license">AL Lic #5827</div>
      <div class="social"><span class="social-square"></span>Socialpage</div>
    </div>

    <div class="divider"></div>

    <ul class="contact">
      <li class="small"><svg viewBox="0 0 26 24"><path class="solid" d="M1 10 L13 2 L25 10 Z"/><rect x="4" y="11" width="18" height="11"/><line x1="13" y1="11" x2="13" y2="22"/></svg>2870 Fenwick Hollow Loop Dothan, AL 36301</li>
      <li><svg viewBox="0 0 26 24"><path class="solid" d="M6 2 L10 2 L11 7 L8 9 Q10 15 14 18 L16 15 L21 16 L21 20 Q19 23 15 22 Q5 17 4 6 Q4 3 6 2 Z"/></svg>334-555-0148</li>
      <li><svg viewBox="0 0 26 24"><rect x="7" y="2" width="12" height="7"/><rect x="3" y="9" width="20" height="12"/><line x1="7" y1="14" x2="19" y2="14"/><line x1="7" y1="18" x2="19" y2="18"/></svg>334-555-0193</li>
      <li class="small"><svg viewBox="0 0 26 24"><rect x="2" y="5" width="22" height="14"/><path d="M2 5 L13 14 L24 5"/></svg>dpelley@tamblynkeys.com</li>
      <li class="small"><svg viewBox="0 0 26 24"><circle cx="13" cy="12" r="10"/><ellipse cx="13" cy="12" rx="4.5" ry="10"/><line x1="3" y1="12" x2="23" y2="12"/><line x1="13" y1="2" x2="13" y2="22"/></svg>www.tamblynkeys.com</li>
    </ul>

    <div class="services"><span>Locksmith • Safes • Security Systems • Camera Systems • Home Theater • Chip Keys &amp; Remotes</span></div>
  </div>
</body>
</html>
```